Business Card Design

Attached is the logo of the store.

Information needed on the business card:

www.brookvale17vino.com
info@brookvale17vino.com
412 Harlow St NY, NY 10027
Tel:(646) 472-3958

Store Hours
Mon-Sat Noon-10pm
Sun Noon-8pm

Free Deliveries

Industry/Entity Type

Business

Contact Information for Business Card

Brookvale 17 Wine & Spirits

```html
<!DOCTYPE html>
<html lang="en">
<head>
<meta charset="UTF-8">
<title>Brookvale 17 Wine &amp; Spirits — Business Card</title>
<link rel="stylesheet" href="https://fonts.googleapis.com/css2?family=Arimo:wght@400;700&display=swap">
<style>
  :root {
    --page-bg: #ffffff;
    --card-bg: #000000;
    --card-text: #ffffff;
    --divider: #ffffff;
  }
  html, body {
    margin: 0;
    padding: 0;
    width: 923px;
    height: 1200px;
    overflow: hidden;
    background: var(--page-bg);
  }
  .canvas {
    position: relative;
    width: 923px;
    height: 1200px;
    font-family: "Arimo", Arial, sans-serif;
    color: var(--card-text);
  }
  .card {
    position: absolute;
    left: 0;
    width: 923px;
    background: var(--card-bg);
    border-radius: 26px;
    overflow: hidden;
  }
  .card--front { top: 0; height: 585px; }
  .card--back { top: 607px; height: 593px; }

  .brand-name {
    position: absolute;
    left: 0;
    right: 0;
    top: 300px;
    margin: 0;
    text-align: center;
    font-weight: 700;
    font-size: 52px;
    letter-spacing: 1px;
    color: var(--card-text);
  }

  .contact-block {
    position: absolute;
    top: 213px;
    right: 422px;
    text-align: right;
  }
  .hours-block {
    position: absolute;
    top: 213px;
    left: 535px;
    text-align: left;
  }
  .info-line {
    margin: 0;
    font-weight: 700;
    font-size: 26px;
    line-height: 42px;
    white-space: nowrap;
  }
  .divider {
    position: absolute;
    left: 516px;
    top: 213px;
    width: 2px;
    height: 168px;
    background: var(--divider);
  }
</style>
</head>
<body>
<div class="canvas">
  <section class="card card--front">
    <h1 class="brand-name">Brookvale 17 Wine &amp; Spirits</h1>
  </section>

  <section class="card card--back">
    <div class="contact-block">
      <p class="info-line">www.brookvale17vino.com</p>
      <p class="info-line">info@brookvale17vino.com</p>
      <p class="info-line">412 Harlow St NY, NY 10027</p>
      <p class="info-line">Tel:(646) 472-3958</p>
    </div>
    <div class="divider"></div>
    <div class="hours-block">
      <p class="info-line">Store Hours</p>
      <p class="info-line">Mon-Sat Noon-10pm</p>
      <p class="info-line">Sun Noon-8pm</p>
      <p class="info-line">Free Deliveries</p>
    </div>
  </section>
</div>
</body>
</html>
```